Poster for a Theatre production!

Create a poster (11 by 17) promoting an upcoming theatre production. The play is called THE HOLLOW LANTERN by Marcus T. Penwell . The play is a fusion of the absurd and realism and has a quantum physics/ mechanics slant fyi. I would like primarily a dark/black background with white print. there should be quantum physics imagery , (squiggly lines/ atoms etc. celestial even...) in the background as well . The
THE HOLLOW LANTERN letters Should Start out white as though ' painted ' (this is important.)and gradually fade to grey or white and black (Still visable though) . To be included also - 'Theatre Olvenk presents' (top of poster and about 1/3 the size) then THE HOLLOW LANTERN ' by Marcus T Penwell' and Half the size of the Title. Also included in print ' Directed by Gregor Lindqvist' and the words 'with' Margaret Solvane, Tim Orcutt and and Rosalind Petrakis Also in small print 'Video design by Corinne Valdez'. The poster also Needs the Dates ' Dec 7-16th ,The Fenwick Loft , 418 Marlowe Street 555 318-4096 '

Target Market(s)

Theatre going audience

Font styles to use
Other font styles liked:
• white painted effect on THE HOLLOW LANTERN

Colors
1b1b1b
fbfbfb
cbcbcb
dddddd
d5d5d5
5c5c5c
333333

Requirements
Must have
• Theatre Olvenk presents THE HOLLOW LANTERN by Marcus T Penwell . Directed by Gregor Lindqvist ( THIS THE CAST FYI)'with' Margaret Solvane, Tim Orcutt, Rosalynde Petrackis . Video design by Corinne Valdez. Dec 7-16th , The Fenwick Loft 418 Marlowe Street 555 318 4096 Black backgroud , painting effect on THE HOLLOW LANTERN . Quantum physics imagery background (SEE UP LOADED FILE) disregard human image
Nice to have
• IF YOU CAN INCORPORATE A HURTLING CHRISTMAS TREE THRU SPACE (RED & GREEN LIGHTS) THAT WOULD BE FANTASTiC see upload!! Christmas tree moving thru space as rocket..
Should not have
• COLOR -Except lights on Christmas tree

```html
<!DOCTYPE html>
<html lang="en">
<head>
<meta charset="utf-8">
<title>The Hollow Lantern — Theatre Olvenk</title>
<link rel="stylesheet" href="https://fonts.googleapis.com/css2?family=Creepster&family=Montserrat:wght@300;400&family=Rajdhani:wght@500;600&display=swap">
<style>
  :root {
    --page: #f2f2f2;
    --ink: #060606;
    --white: #fbfbfb;
    --light: #dddddd;
    --silver: #cbcbcb;
    --mid: #9a9a9a;
    --grey: #5c5c5c;
    --dark: #333333;
  }
  * { margin: 0; padding: 0; box-sizing: border-box; }
  html, body {
    width: 1062px;
    height: 1200px;
    overflow: hidden;
    background: var(--page);
  }
  .poster {
    position: absolute;
    left: 151px;
    top: 20px;
    width: 760px;
    height: 1160px;
    background: var(--ink);
    color: var(--white);
    text-align: center;
  }
  .poster > * { position: absolute; left: 0; width: 100%; }

  .company {
    top: 30px;
    font: 400 31px/1 "Montserrat", sans-serif;
    letter-spacing: 0.42em;
    padding-left: 0.42em;
  }
  .presents {
    top: 80px;
    font: 500 24px/1 "Rajdhani", sans-serif;
    letter-spacing: 0.16em;
  }
  .quantum-art {
    top: 218px;
    left: 71px;
    width: 591px;
    height: 218px;
    background: radial-gradient(ellipse at 62% 45%, #3a3a3a 0%, #1b1b1b 45%, var(--ink) 80%);
    border-radius: 50%;
  }
  .title {
    top: 515px;
    font: 400 78px/1 "Creepster", sans-serif;
    letter-spacing: 0.03em;
  }
  .title span {
    display: block;
    margin-bottom: 4px;
    background: linear-gradient(180deg, var(--white) 0%, var(--light) 45%, var(--grey) 100%);
    -webkit-background-clip: text;
    background-clip: text;
    color: transparent;
  }
  .author {
    top: 822px;
    font: 400 25px/1 "Montserrat", sans-serif;
    letter-spacing: 0.16em;
    color: var(--mid);
  }
  .credits {
    top: 885px;
    font: 600 13.5px/19.5px "Rajdhani", sans-serif;
    letter-spacing: 0.3em;
    color: var(--light);
  }
  .dates {
    top: 1050px;
    font: 500 56px/1 "Rajdhani", sans-serif;
    letter-spacing: 0.12em;
    padding-left: 0.12em;
  }
  .dates sup {
    font-size: 24px;
    vertical-align: top;
    position: relative;
    top: -4px;
    letter-spacing: 0.1em;
  }
  .atom {
    left: 577px;
    top: 990px;
    width: 142px;
    height: 100px;
  }
  .venue {
    top: 1118px;
    left: 85px;
    width: auto;
    text-align: left;
    font: 500 13.5px/1 "Rajdhani", sans-serif;
    letter-spacing: 0.22em;
    color: var(--light);
  }
</style>
</head>
<body>
  <main class="poster">
    <p class="company">THEATRE OLVENK</p>
    <p class="presents">PRESENTS</p>

    <div class="quantum-art" role="img" aria-label="Particle-track drawing of spiralling quantum orbits in white on black"></div>

    <h1 class="title">
      <span>THE</span>
      <span>HOLLOW</span>
      <span>LANTERN</span>
    </h1>

    <p class="author">BY MARCUS T PENWELL</p>

    <p class="credits">
      DIRECTED BY GREGOR LINDQVIST<br>
      WITH<br>
      MARGARET SOLVANE | TIM ORCUTT | ROSALYNDE PETRACKIS<br>
      VIDEO DESIGN BY CORINNE VALDEZ
    </p>

    <p class="dates">DEC 7-16<sup>TH</sup></p>

    <svg class="atom" viewBox="0 0 142 100" aria-hidden="true">
      <g fill="none" stroke="#5c5c5c" stroke-width="3">
        <ellipse cx="71" cy="50" rx="66" ry="20"/>
        <ellipse cx="71" cy="50" rx="66" ry="20" transform="rotate(60 71 50)"/>
        <ellipse cx="71" cy="50" rx="66" ry="20" transform="rotate(-60 71 50)"/>
      </g>
      <g fill="#5c5c5c">
        <circle cx="71" cy="50" r="8"/>
        <circle cx="8" cy="46" r="5"/>
        <circle cx="104" cy="8" r="5"/>
        <circle cx="40" cy="94" r="5"/>
      </g>
    </svg>

    <p class="venue">THE FENWICK LOFT, 418 MARLOWE STREET 555 318-4096</p>
  </main>
</body>
</html>
```